Neighbourhood assistance

I need an app design for a social idea. Each person has some skils and could offer some assistance to some of his neighbours. With this app I will bring people together. For free or also for some money.That doesn't matter.

Please have a look into my pptx file which should give you an idea about the upcoming app.

Industry/Entity Type

Social

```html
<!DOCTYPE html>
<html lang="de">
<head>
<meta charset="utf-8">
<title>Helferviertel – Start</title>
<link rel="stylesheet" href="https://fonts.googleapis.com/css2?family=Arimo:wght@400;500&family=Dosis:wght@400;500&family=Raleway:wght@300;400&display=swap">
<style>
  :root {
    --bg: #ffffff;
    --ink: #000000;
    --brand-purple: #9a12c4;
    --body-grey: #5a5a5a;
    --action-green: #0fd38a;
    --action-text: #ffffff;
    --town-light: #cfd86a;
    --town-mid: #a6bb43;
    --town-dark: #7f9a35;
  }
  * { box-sizing: border-box; margin: 0; padding: 0; }
  html, body {
    width: 676px; height: 1200px; overflow: hidden;
    background: var(--bg);
  }
  .screen {
    position: relative; width: 676px; height: 1200px;
    background: var(--bg); overflow: hidden;
  }
  .status-bar {
    position: absolute; top: 0; left: 0; width: 100%; height: 42px;
    font-family: "Arimo", Helvetica, sans-serif; font-size: 22px; font-weight: 500;
    color: var(--ink);
  }
  .status-bar .signal { position: absolute; left: 15px; top: 13px; }
  .status-bar .carrier { position: absolute; left: 101px; top: 8px; }
  .status-bar .wifi { position: absolute; left: 175px; top: 10px; }
  .status-bar .clock { position: absolute; left: 0; right: 0; top: 8px; text-align: center; }
  .status-bar .rotation-lock { position: absolute; left: 504px; top: 10px; }
  .status-bar .battery-level { position: absolute; left: 540px; top: 8px; }
  .status-bar .battery { position: absolute; left: 614px; top: 12px; }

  .app-mark {
    position: absolute; left: 277px; top: 182px;
    width: 148px; height: 148px; border-radius: 50%;
    background: var(--brand-purple);
  }
  .app-name {
    position: absolute; left: 0; right: 0; top: 364px;
    text-align: center;
    font-family: "Dosis", sans-serif; font-weight: 400; font-size: 52px;
    line-height: 60px; letter-spacing: 2px; color: var(--brand-purple);
  }
  .intro {
    position: absolute; left: 0; right: 0; top: 464px;
    text-align: center;
    font-family: "Raleway", sans-serif; font-weight: 400; font-size: 19px;
    line-height: 27px; color: var(--body-grey);
  }
  .continue-button {
    position: absolute; left: 116px; top: 582px;
    width: 482px; height: 84px; border: 0; border-radius: 4px;
    background: var(--action-green); color: var(--action-text);
    font-family: "Raleway", sans-serif; font-weight: 300; font-size: 29px;
    display: flex; align-items: center; justify-content: center;
  }
  .townscape {
    position: absolute; left: 0; bottom: 0; width: 676px; height: 160px;
    background: linear-gradient(to bottom, rgba(207,216,106,0) 0%, rgba(207,216,106,0.55) 35%, var(--town-mid) 85%, var(--town-dark) 100%);
  }
</style>
</head>
<body>
<div class="screen">
  <header class="status-bar">
    <svg class="signal" width="80" height="14" viewBox="0 0 80 14" aria-hidden="true">
      <circle cx="7" cy="7" r="6" fill="#000"/>
      <circle cx="23" cy="7" r="6" fill="#000"/>
      <circle cx="39" cy="7" r="6" fill="#000"/>
      <circle cx="55" cy="7" r="6" fill="#000"/>
      <circle cx="71" cy="7" r="5.3" fill="none" stroke="#000" stroke-width="1.4"/>
    </svg>
    <span class="carrier">Nexa</span>
    <svg class="wifi" width="24" height="20" viewBox="0 0 24 20" aria-hidden="true">
      <path d="M12 19 L8 14.5 A6 6 0 0 1 16 14.5 Z" fill="#000"/>
      <path d="M4.5 10.5 A11 11 0 0 1 19.5 10.5" fill="none" stroke="#000" stroke-width="2.6"/>
      <path d="M1 6.5 A16 16 0 0 1 23 6.5" fill="none" stroke="#000" stroke-width="2.6"/>
    </svg>
    <span class="clock">4:20 PM</span>
    <svg class="rotation-lock" width="22" height="22" viewBox="0 0 22 22" aria-hidden="true">
      <path d="M18 6 A9 9 0 1 0 20 11" fill="none" stroke="#000" stroke-width="2"/>
      <path d="M15 5 L19 6 L19 2" fill="none" stroke="#000" stroke-width="2"/>
      <rect x="7" y="10" width="8" height="6" fill="#000"/>
      <path d="M8.5 10 V8 a2.5 2.5 0 0 1 5 0 V10" fill="none" stroke="#000" stroke-width="1.6"/>
    </svg>
    <span class="battery-level">100%</span>
    <svg class="battery" width="52" height="20" viewBox="0 0 52 20" aria-hidden="true">
      <rect x="1" y="1" width="45" height="18" rx="3" fill="none" stroke="#000" stroke-width="1.6"/>
      <rect x="3.5" y="3.5" width="40" height="13" rx="1.5" fill="#000"/>
      <rect x="47.5" y="6.5" width="3" height="7" rx="1" fill="#000"/>
    </svg>
  </header>

  <main>
    <div class="app-mark" aria-hidden="true"></div>
    <h1 class="app-name">HELFERVIERTEL</h1>
    <p class="intro">Jeder kann in irgend einer Form jemand anderes<br>unterstützen. Darum geht es in dieser App.</p>
    <button class="continue-button" type="button">Weiter</button>
  </main>

  <div class="townscape" role="img" aria-label="Green illustrated neighbourhood skyline with houses, trees, a bicycle, birds, clouds, a sun, tall buildings and a hot-air balloon"></div>
</div>
</body>
</html>
```